Trvmlegal.com needs a wedsite. Law Office of Darnell P. Whitby

Darnell P. Whitby is a criminal law firm that is 5 years old. We have already had all the content written and now just need the website designed. We also just finished our logo design using Pixel Harbor and would like it used in the design of the website.

Industry/Entity Type

Law Firm

Number of Pages Required

5+ page

Requirements
Must have
• I was our new logo to be on the website also. I want Dallas sites as the stock pictures for the website. For example the Grey Stone Tribunal. I also need to be able to add YouTube videos. It has to adjust to be seen on computers and also cell phones. I need to be able to have a information sheet for clients to fill out and submit back to me.

```html
<!DOCTYPE html>
<html lang="en">
<head>
<meta charset="utf-8">
<title>Law Office of Darnell P. Whitby</title>
<link rel="stylesheet" href="https://fonts.googleapis.com/css2?family=Cinzel:wght@400;700&family=Open+Sans:wght@400;600;700&family=Arimo:wght@400;700&display=swap">
<style>
:root{
  --navy:#0b2a66;
  --navy-deep:#061d4d;
  --navy-mid:#123a80;
  --silver:#c9ccd1;
  --panel:#2b2e33;
  --page:#e8e8e8;
  --white:#ffffff;
  --ink:#1b1b1b;
  --bronze:#9b5a0a;
  --link:#0b2a66;
  --cream:#f3dcae;
}
*{margin:0;padding:0;box-sizing:border-box}
html,body{width:1155px;height:1200px;overflow:hidden}
body{position:relative;background:var(--page);font-family:'Open Sans',sans-serif;color:var(--ink)}
.abs{position:absolute}

.site-header{left:0;top:0;width:1155px;height:89px;background:linear-gradient(#0a2c6c,#06204f)}
.header-rule{left:0;top:89px;width:1155px;height:10px;background:linear-gradient(#e6e7ea,#a9adb4)}
.nav-item{top:30px;font-family:'Cinzel',serif;font-size:12.5px;line-height:15px;color:var(--white);letter-spacing:.5px}
.nav-divider{top:16px;width:1px;height:56px;background:#1f4690}

.brand-badge{left:512px;top:6px;width:122px;height:122px;border-radius:50%;background:var(--navy-deep);border:4px solid #8fa4c9;display:flex;align-items:center;justify-content:center;text-align:center}
.brand-badge span{font-family:'Cinzel',serif;font-weight:700;font-size:13px;line-height:17px;color:var(--white)}

.hero{left:0;top:99px;width:1155px;height:403px;background:linear-gradient(90deg,#5c5e62 0%,#8b8e92 25%,#3c3e42 50%,#6d7074 75%,#a5a7aa 100%)}
.hero-copy{left:574px;top:207px;width:380px;color:var(--white)}
.hero-title{font-family:'Cinzel',serif;font-size:21px;line-height:24px;font-weight:400}
.hero-lead{font-size:11px;line-height:14px;margin-top:6px}
.hero-call{font-size:14.5px;font-weight:700;margin-top:8px;line-height:20px}
.hero-call a{color:var(--cream);text-decoration:underline}

.content-panel{left:165px;top:487px;width:825px;height:530px;background:var(--white)}
.rights-box{left:175px;top:495px;width:806px;height:117px;background:var(--panel);border:1px solid #9ea3a8;padding:14px 21px}
.rights-box h1{font-family:'Cinzel',serif;font-size:21.5px;font-weight:400;color:var(--white);letter-spacing:.4px}
.rights-box p{font-size:11px;line-height:14px;color:#d6d7d9;margin-top:12px}

.team-heading{left:185px;top:645px;font-family:'Cinzel',serif;font-size:21px;color:#2a2c30;letter-spacing:.5px}
.avatar{width:82px;height:82px;border-radius:50%;background:radial-gradient(circle at 50% 40%,#d9b59a,#efe6da 70%)}
.member{width:230px;font-size:11.8px;line-height:14px;color:#222}
.member-name{font-family:'Arimo',sans-serif;font-weight:700;font-size:13.5px;color:var(--bronze);margin-top:8px}
.read-more{font-family:'Arimo',sans-serif;font-size:9.5px;color:var(--link);margin-top:2px;display:block}

.site-footer{left:0;top:1004px;width:1155px;height:196px;background:linear-gradient(160deg,#0b2a66,#061a47 60%,#0a2b68)}
.footer-badge{left:184px;top:1042px;width:89px;height:89px;border-radius:50%;background:var(--navy);border:3px solid #8fa4c9;display:flex;align-items:center;justify-content:center;text-align:center}
.footer-badge span{font-family:'Cinzel',serif;font-weight:700;font-size:10px;line-height:13px;color:var(--white)}
.footer-title{font-family:'Cinzel',serif;font-size:16px;color:var(--white);padding-bottom:3px;border-bottom:1px solid #c3cbe0}
.quick-title{left:304px;top:1038px;width:359px}
.contact-title{left:720px;top:1038px;width:270px}
.footer-links{list-style:none;font-size:10px;color:var(--white)}
.footer-links li{height:20px;line-height:14px}
.contact-row{left:720px;font-size:10.5px;color:var(--white);display:flex;align-items:center;gap:8px}
.contact-row svg{width:14px;height:14px}
</style>
</head>
<body>

<header class="site-header abs"></header>
<div class="header-rule abs"></div>

<nav>
  <div class="nav-item abs" style="left:202px">ATTORNEY<br>PROFILES</div>
  <div class="nav-divider abs" style="left:297px"></div>
  <div class="nav-item abs" style="left:319px">HOW WE<br>CAN HELP</div>
  <div class="nav-divider abs" style="left:402px"></div>
  <div class="nav-item abs" style="left:426px">Case<br>Offenses</div>
  <div class="nav-item abs" style="left:648px">Expungements &amp;<br>Non-Disclosures</div>
  <div class="nav-divider abs" style="left:787px"></div>
  <div class="nav-item abs" style="left:805px">PROBATIONS<br>&amp; VIOLATIONS</div>
  <div class="nav-divider abs" style="left:913px"></div>
  <div class="nav-item abs" style="left:939px">DWI,<br>DUI</div>
</nav>

<section class="hero abs" role="img" aria-label="Photo of an attorney in a grey suit holding a briefcase inside a courtroom, with scales of justice on the right"></section>
<div class="brand-badge abs"><span>Law Office of<br>Darnell P.<br>Whitby</span></div>

<div class="hero-copy abs">
  <h2 class="hero-title">Our Aggressive Criminal<br>Defense Team Fights for You</h2>
  <p class="hero-lead">Our Dallas-Fort Worth law firm solely handles criminal defense cases so we can dedicate our full resources to the pursuit of justice.</p>
  <p class="hero-call">Call the Law Office &nbsp;at 972.555.0148<br>or <a>contact us online</a></p>
</div>

<main>
  <div class="content-panel abs"></div>
  <section class="rights-box abs">
    <h1>OUR DALLAS ATTORNEYS PROTECT YOUR RIGHTS TO JUSTICE</h1>
    <p>You have the right to remain silent and to have an attorney present for questioning. You should exercise these constitutional rights when charged with a serious crime. Do not say anything since even a seemingly innocent statement could lead to incriminating evidence and trying to talk your way out of it could have the opposite effect. Ask for a lawyer then call the Law Office of Darnell P. Whitby for help.</p>
  </section>

  <h2 class="team-heading abs">MEET OUR CRIMINAL DEFENSE TEAM:</h2>

  <div class="avatar abs" style="left:258px;top:707px" role="img" aria-label="Portrait of Milo Harrowgate"></div>
  <div class="avatar abs" style="left:524px;top:707px" role="img" aria-label="Portrait of Darnell P. Whitby"></div>
  <div class="avatar abs" style="left:800px;top:707px" role="img" aria-label="Portrait of Renata Solis-Vane"></div>

  <article class="member abs" style="left:202px;top:817px">
    <p>Vel illum dolore eu feugiat nulla facilisis at vero eros et accumsan et iusto dignissim qui blandit praesent lupt zril delenit augue duis dolore te feugait nulla facilisi.</p>
    <div class="member-name">Milo Harrowgate</div>
    <a class="read-more">read more +</a>
  </article>
  <article class="member abs" style="left:465px;top:817px">
    <p>Typi non habent claritatem insitam est us legentis in iis qui facit eorum claritatem. Investigationes demonstraverunt lectores legere me lius quod ii legunt saepius.</p>
    <div class="member-name">Darnell P. Whitby</div>
    <a class="read-more">read more +</a>
  </article>
  <article class="member abs" style="left:737px;top:817px">
    <p>Claritas est etiam processus dynamicus sequitur mutationem consuetudium lectorum. Mirum est notare quam littera gothica, quam nunc pumus parum clam, anteposuerit litterarum formas.</p>
    <div class="member-name">Renata Solis-Vane</div>
    <a class="read-more">read more +</a>
  </article>
</main>

<footer class="site-footer abs"></footer>
<div class="footer-badge abs"><span>Darnell P.<br>Whitby</span></div>

<h3 class="footer-title quick-title abs">QUICK LINKS</h3>
<ul class="footer-links abs" style="left:305px;top:1071px">
  <li>ATTORNEY PROFILE</li>
  <li>HOW WE CAN HELP</li>
  <li>MURDER &amp; OTHER HOMICIDE OFFENSES</li>
  <li>SEXUAL OFFENSES</li>
  <li>EXPUNGEMENTS &amp; NON-DISCLOSURES</li>
</ul>
<ul class="footer-links abs" style="left:536px;top:1071px">
  <li>EARLY PROBATION RELEASE</li>
  <li>PROBATION VIOLATIONS</li>
  <li>OTHER VIOLENT OFFENSES</li>
  <li>DWI, DUI</li>
  <li>DRUG OFFENSES</li>
</ul>

<h3 class="footer-title contact-title abs">CONTACT US</h3>
<div class="contact-row abs" style="top:1074px">
  <svg viewBox="0 0 14 14"><path d="M7 1a4 4 0 0 0-4 4c0 3 4 8 4 8s4-5 4-8a4 4 0 0 0-4-4z" fill="none" stroke="#fff" stroke-width="1.6"/><circle cx="7" cy="5" r="1.4" fill="#fff"/></svg>
  <span>48 Elm Row, Dallas, Texas, USA</span>
</div>
<div class="contact-row abs" style="top:1098px">
  <svg viewBox="0 0 14 14"><rect x="1" y="3" width="12" height="8" fill="#fff"/><path d="M1 3l6 5 6-5" fill="none" stroke="#0b2a66" stroke-width="1"/></svg>
  <span>contact@Trvmlegal.com</span>
</div>
<div class="contact-row abs" style="top:1121px">
  <svg viewBox="0 0 14 14"><path d="M3 2l2 0 1 3-1.5 1a7 7 0 0 0 3.5 3.5l1-1.5 3 1 0 2c-5 1-10-4-9-9z" fill="#fff"/></svg>
  <span>972.555.0148</span>
</div>

</body>
</html>
```